Online retailer needs a Quirky yet professionally designed double sided business car

We mainly sell kitchen and home accessories but pretty much anything new and in demand. Have a look at our site and then come up with designs.
Design to be really catching and want people to visit the website.
Final details such as number, director name and email address will be given to the designer of the winning business card.

Www.zapfinda.com

Ideas out of the norm also welcome!!

```html
<!DOCTYPE html>
<html lang="en">
<head>
<meta charset="utf-8">
<title>Zapfinda Business Card</title>
<link href="https://fonts.googleapis.com/css2?family=Quicksand:wght@600&family=Noto+Serif:wght@400&display=swap" rel="stylesheet">
<style>
  :root {
    --canvas: #e9e7e4;
    --card-dark: #2a2727;
    --card-light: #ffffff;
    --ink: #231f20;
    --orange: #ef7d1a;
    --text-light: #f2f0ee;
    --rule: #3a3636;
    --divider: #4a4545;
  }
  * { box-sizing: border-box; margin: 0; padding: 0; }
  html, body {
    width: 1200px; height: 914px; overflow: hidden;
    background: var(--canvas);
  }
  .canvas { position: relative; width: 1200px; height: 914px; }
  .card {
    position: absolute; left: 240px; width: 720px; height: 412px;
    box-shadow: 0 6px 18px rgba(0,0,0,0.18);
    overflow: hidden;
  }

  /* Back side */
  .card--back { top: 36px; background: var(--card-dark); }
  .back__band {
    position: absolute; left: 0; top: 0; bottom: 0; width: 16px;
    background: var(--orange);
  }
  .back__band-line {
    position: absolute; left: 26px; top: 0; bottom: 0; width: 2px;
    background: var(--orange); opacity: .55;
  }
  .back__name {
    position: absolute; left: 28px; width: 332px; top: 50%;
    transform: translateY(-50%); text-align: center;
    font-family: 'Noto Serif', serif; font-weight: 400;
    font-size: 42px; line-height: 1; color: var(--orange);
  }
  .back__divider {
    position: absolute; left: 360px; top: 40px; bottom: 40px; width: 1px;
    background: var(--divider);
  }
  .contact {
    position: absolute; left: 400px; top: 88px;
    font-family: 'Noto Serif', serif; color: var(--text-light);
  }
  .contact__name { font-size: 22px; color: var(--orange); margin-bottom: 26px; }
  .contact__list { list-style: none; }
  .contact__item {
    display: flex; align-items: center; gap: 16px;
    font-size: 19px; margin-bottom: 20px; white-space: nowrap;
  }
  .contact__icon { width: 20px; height: 20px; flex: none; }

  /* Front side */
  .card--front { top: 466px; background: var(--card-light); }
  .front__logo {
    position: absolute; left: 0; right: 0; top: 118px; text-align: center;
  }
  .front__name {
    font-family: 'Noto Serif', serif; font-weight: 400;
    font-size: 88px; line-height: 1.05; color: var(--ink);
  }
  .front__tagline-row {
    display: flex; align-items: center; justify-content: center;
    gap: 12px; margin-top: 16px;
  }
  .front__rule { height: 2px; width: 110px; background: var(--ink); }
  .front__tagline {
    font-family: 'Quicksand', sans-serif; font-weight: 600;
    font-size: 26px; color: var(--orange); letter-spacing: .5px;
  }
  .front__footer {
    position: absolute; left: 0; right: 0; bottom: 0; height: 16px;
    background: var(--rule);
  }
</style>
</head>
<body>
<main class="canvas">

  <section class="card card--back" aria-label="Business card back">
    <div class="back__band"></div>
    <div class="back__band-line"></div>
    <p class="back__name">Zapfinda</p>
    <div class="back__divider"></div>
    <div class="contact">
      <p class="contact__name">Your Name</p>
      <ul class="contact__list">
        <li class="contact__item">
          <svg class="contact__icon" viewBox="0 0 20 20"><path d="M10 1a6 6 0 0 0-6 6c0 5 6 12 6 12s6-7 6-12a6 6 0 0 0-6-6zm0 8.5A2.5 2.5 0 1 1 10 4.5a2.5 2.5 0 0 1 0 5z" fill="#f2f0ee"/></svg>
          <span>27, Sample Street, NA</span>
        </li>
        <li class="contact__item">
          <svg class="contact__icon" viewBox="0 0 20 20"><rect x="5" y="1" width="10" height="18" rx="2" fill="none" stroke="#f2f0ee" stroke-width="1.8"/><circle cx="10" cy="16" r="1" fill="#f2f0ee"/></svg>
          <span>0987 654 321</span>
        </li>
        <li class="contact__item">
          <svg class="contact__icon" viewBox="0 0 20 20"><rect x="1.5" y="4" width="17" height="12" fill="#f2f0ee"/><path d="M1.5 4l8.5 7 8.5-7" fill="none" stroke="#2a2727" stroke-width="1.4"/></svg>
          <span>xyz_ab@zapfinda.com</span>
        </li>
        <li class="contact__item">
          <svg class="contact__icon" viewBox="0 0 20 20"><circle cx="10" cy="10" r="8.5" fill="none" stroke="#f2f0ee" stroke-width="1.6"/><ellipse cx="10" cy="10" rx="3.5" ry="8.5" fill="none" stroke="#f2f0ee" stroke-width="1.3"/><path d="M1.5 10h17M3 6h14M3 14h14" stroke="#f2f0ee" stroke-width="1.2"/></svg>
          <span>Www.zapfinda.com</span>
        </li>
      </ul>
    </div>
  </section>

  <section class="card card--front" aria-label="Business card front">
    <div class="front__logo">
      <p class="front__name">Zapfinda</p>
      <div class="front__tagline-row">
        <span class="front__rule"></span>
        <span class="front__tagline">kitchen and home finds</span>
        <span class="front__rule"></span>
      </div>
    </div>
    <div class="front__footer"></div>
  </section>

</main>
</body>
</html>
```